Full re-design of visual identity

We have just re-designed our logo and would like to apply it on our folders, business cards, stationery, and etc... we are attaching new logo + the material we need to re-design... we will provide full corel draw files to help make job easier and also because lot of icons and artwork can be still used...

any doubts we are at your disposal. thanks in advance.

```html
<!DOCTYPE html>
<html lang="en">
<head>
<meta charset="utf-8">
<title>Corvano business card</title>
<link rel="stylesheet" href="https://fonts.googleapis.com/css2?family=Arimo:wght@400;700&display=swap">
<style>
  :root {
    --backdrop: #e9e7e4;
    --card: #ffffff;
    --orange: #e8731f;
    --grey: #8a8a8a;
    --grey-band: #a3a3a3;
    --ink: #2b2b2b;
    --label: #555555;
    --rule: #d8d8d8;
  }
  * { box-sizing: border-box; margin: 0; padding: 0; }
  html, body {
    width: 1200px; height: 900px; overflow: hidden;
    background: var(--backdrop);
    font-family: "Arimo", Arial, sans-serif;
  }
  .sheet {
    width: 1200px; height: 900px;
    display: flex; flex-direction: column;
    align-items: center; justify-content: center; gap: 44px;
  }
  .card {
    position: relative;
    width: 672px; height: 384px;
    background: var(--card);
    box-shadow: 0 2px 10px rgba(0,0,0,0.12);
    overflow: hidden;
  }
  /* front */
  .brand {
    position: absolute; left: 40px; top: 0; width: 300px; height: 354px;
    display: flex; align-items: center; justify-content: center;
  }
  .brand-name {
    font-size: 60px; font-weight: 700; color: var(--grey);
    letter-spacing: -1px; line-height: 1;
  }
  .divider {
    position: absolute; left: 372px; top: 26px; width: 1px; height: 270px;
    background: var(--rule);
    box-shadow: -6px 0 10px rgba(0,0,0,0.07);
  }
  .contact {
    position: absolute; left: 400px; top: 26px; right: 20px;
    color: var(--label);
  }
  .person-name { font-size: 22px; color: var(--orange); }
  .person-role { font-size: 16px; color: var(--ink); margin-top: 2px; }
  .details { margin-top: 36px; font-size: 13px; line-height: 1.35; }
  .details dt { font-weight: 700; text-transform: uppercase; color: var(--ink); }
  .details dd { color: var(--label); margin-bottom: 2px; }
  .footer-band {
    position: absolute; left: 0; right: 0; bottom: 0; height: 30px;
    display: flex;
  }
  .footer-accent { flex: 0 0 58%; background: var(--orange); }
  .footer-web {
    flex: 1; background: var(--grey-band); color: #fff;
    font-size: 15px; display: flex; align-items: center; justify-content: flex-end;
    padding-right: 22px;
  }
  /* back */
  .card-back {
    display: flex; align-items: center; justify-content: center; gap: 18px;
  }
  .back-mark {
    width: 34px; height: 34px; border-radius: 50%; background: var(--orange);
  }
  .back-name {
    font-size: 72px; font-weight: 700; color: var(--orange);
    letter-spacing: -1px; line-height: 1;
  }
</style>
</head>
<body>
<main class="sheet">
  <section class="card card-front">
    <div class="brand">
      <div class="brand-name">Corvano</div>
    </div>
    <div class="divider"></div>
    <div class="contact">
      <div class="person-name">Daniel Reyes</div>
      <div class="person-role">President</div>
      <dl class="details">
        <dt>Address:</dt><dd>48 Linden Avenue, VA, 22040</dd>
        <dt>Phone:</dt><dd>600 418 2207</dd>
        <dt>Fax:</dt><dd>600 418 2208</dd>
        <dt>Email:</dt><dd>hello@corvano-net.com</dd>
      </dl>
    </div>
    <div class="footer-band">
      <div class="footer-accent"></div>
      <div class="footer-web">www.corvano-net.com</div>
    </div>
  </section>
  <section class="card card-back">
    <span class="back-mark"></span>
    <span class="back-name">Corvano</span>
  </section>
</main>
</body>
</html>
```